BrookhavenLLC

Real Estate Investment. Buy/Sell house/investment . Trustworthy,Reliable, and friendly

Industry/Entity Type

Real Estate

Contact Information for Business Card

Brookhaven@mailbox-example.com
808-555-0143
Linnea-Joy Patterson

```html
<!DOCTYPE html>
<html lang="en">
<head>
<meta charset="utf-8">
<title>BrookhavenLLC — Business Card</title>
<link rel="stylesheet" href="https://fonts.googleapis.com/css2?family=Bodoni+Moda:wght@400&family=Jost:wght@400&family=Great+Vibes&display=swap">
<style>
  :root {
    --backdrop: #e6e4e0;
    --card: #1d2022;
    --card-edge: #25292c;
    --ink-light: #e4e4e2;
    --ink-muted: #d2d3d2;
    --brand-slate: #3c4d57;
    --tagline: #2e3c43;
  }
  * { margin: 0; padding: 0; box-sizing: border-box; }
  html, body {
    width: 1200px;
    height: 800px;
    overflow: hidden;
    background: var(--backdrop);
  }
  .canvas {
    position: relative;
    width: 1200px;
    height: 800px;
  }
  .business-card {
    position: absolute;
    left: 180px;
    top: 160px;
    width: 840px;
    height: 480px;
    background: var(--card);
    border-radius: 10px;
    box-shadow: 0 18px 40px rgba(0,0,0,0.25);
    border: 1px solid var(--card-edge);
  }
  .brand-mark {
    position: absolute;
    left: 50px;
    top: 214px;
    display: flex;
    align-items: center;
    gap: 10px;
  }
  .brand-dot {
    width: 18px;
    height: 18px;
    border-radius: 50%;
    background: var(--brand-slate);
  }
  .brand-name {
    font-family: "Jost", sans-serif;
    font-size: 26px;
    color: var(--brand-slate);
    letter-spacing: 0.5px;
  }
  .card-details {
    position: absolute;
    left: 300px;
    top: 140px;
    width: 500px;
    text-align: center;
  }
  .person-name {
    font-family: "Bodoni Moda", serif;
    font-weight: 400;
    font-size: 44px;
    color: var(--ink-light);
    letter-spacing: 0.5px;
    line-height: 1.1;
  }
  .tagline {
    font-family: "Great Vibes", cursive;
    font-size: 38px;
    color: var(--tagline);
    margin-top: 4px;
    padding-left: 50px;
    line-height: 1.1;
  }
  .contact {
    font-family: "Jost", sans-serif;
    font-size: 29px;
    color: var(--ink-muted);
    line-height: 1.22;
    margin-top: 12px;
  }
</style>
</head>
<body>
  <main class="canvas">
    <section class="business-card">
      <div class="brand-mark">
        <span class="brand-dot"></span>
        <span class="brand-name">BrookhavenLLC</span>
      </div>
      <div class="card-details">
        <h1 class="person-name">Linnea-Joy Patterson</h1>
        <p class="tagline">Trustworthy|Reliable|Friendly</p>
        <p class="contact">Brookhaven@mailbox-example.com<br>808-555-0143</p>
      </div>
    </section>
  </main>
</body>
</html>
```